'Rebuild' the outer box design of foam cleaner

I have had the bottle label designed as attached. But I chose not to assign this project to the original bottle label designer. Because I don't expect the outer box to be cloned with the label, though they should be in a similar style. I hope you guys to work out an exquisite box for the product with your own marks. Of course, I also don't like the box to be designed totally different with the label too. Under the same design rule of the label, the box should have its own characteristics.

Target Market(s)

16-35 female, orthodontic patients.

Requirements
Must have
• 1.Bar code must show on the outer box. But it could be customized to be other styles.
2.All the contents in the document 'OUTERCONTAINERDESIGN' must be involved. Surely designers could add some other reasonable elements.
Nice to have
• it's nice to have the pic of clear aligner involved.
Should not have
• the QR code on the label should not exist on the outer box.

```html
<!DOCTYPE html>
<html lang="en">
<head>
<meta charset="utf-8">
<title>Spriza Aligner Cleaner – Box Dieline</title>
<link rel="stylesheet" href="https://fonts.googleapis.com/css2?family=Open+Sans:wght@400;600;700;800&family=PT+Sans+Narrow:wght@400;700&display=swap">
<style>
  :root {
    --bg: #b3b3b3;
    --blue-light: #0a78c2;
    --blue-mid: #0a4f98;
    --blue-deep: #13306b;
    --blue-text: #1f57b5;
    --white: #ffffff;
    --green: #5a9e58;
    --teal: #3f8c7a;
    --dot: #d6d8de;
  }
  * { box-sizing: border-box; margin: 0; padding: 0; }
  html, body { width: 1200px; height: 750px; overflow: hidden; }
  body {
    background: var(--bg);
    font-family: "Open Sans", sans-serif;
    position: relative;
  }
  .dieline {
    position: absolute;
    left: 0; top: 0;
    width: 1200px; height: 750px;
    display: flex;
    align-items: center;
    justify-content: center;
    gap: 28px;
  }

  /* FRONT PANEL */
  .panel-front {
    position: relative;
    width: 240px; height: 700px;
    background: linear-gradient(180deg, var(--blue-light) 0%, var(--blue-mid) 35%, var(--blue-deep) 68%);
    overflow: hidden;
  }
  .tag-freshness {
    position: absolute;
    top: 26px; left: 20px;
    display: flex; align-items: center; gap: 6px;
  }
  .tag-freshness .label {
    background: var(--white);
    color: var(--blue-mid);
    font-weight: 700;
    font-size: 11px;
    letter-spacing: 1.6px;
    padding: 4px 10px;
  }
  .brand-name {
    position: absolute;
    top: 120px; left: 0; right: 0;
    text-align: center;
    color: var(--white);
    font-weight: 800;
    font-size: 50px;
    letter-spacing: -1px;
  }
  .brand-name .dot {
    display: inline-block;
    width: 12px; height: 12px;
    border: 3px solid var(--white);
    border-radius: 50%;
    margin-left: 3px;
    vertical-align: top;
    margin-top: 10px;
  }
  .product-title {
    position: absolute;
    top: 250px; left: 0; right: 0;
    text-align: center;
    color: var(--white);
    font-weight: 700;
    line-height: 1;
  }
  .product-title .line-small { font-size: 26px; letter-spacing: 1px; }
  .product-title .line-large { font-size: 38px; margin-top: 4px; }
  .supply-band {
    margin: 6px auto 0;
    width: 170px;
    background: linear-gradient(90deg, var(--green), var(--teal));
    color: var(--white);
    font-size: 9px;
    letter-spacing: 3px;
    padding: 4px 0;
    font-weight: 600;
  }
  .aligner-art {
    position: absolute;
    top: 405px; left: 30px;
    width: 180px; height: 90px;
    border-radius: 40px 40px 30px 30px;
    background: radial-gradient(ellipse at center, #ffffff 0%, #e2e6ec 70%, rgba(226,230,236,0) 100%);
  }
  .wave-band {
    position: absolute;
    top: 480px; left: 0;
    width: 240px; height: 70px;
  }
  .lower-white {
    position: absolute;
    top: 515px; left: 0;
    width: 240px; height: 185px;
    background: var(--white);
  }
  .dot-field {
    position: absolute;
    top: 505px; left: 0;
    width: 240px; height: 150px;
    background: linear-gradient(180deg, var(--dot) 0%, rgba(214,216,222,0.4) 60%, rgba(255,255,255,0) 100%);
  }
  .benefits {
    position: absolute;
    top: 560px; left: 24px;
    list-style: none;
    color: var(--blue-text);
    font-weight: 700;
    font-size: 15px;
    line-height: 1.25;
  }
  .benefits li { display: flex; align-items: center; gap: 6px; }
  .net-content {
    position: absolute;
    bottom: 14px; left: 0; right: 0;
    text-align: center;
    color: var(--blue-text);
    font-size: 12px;
  }

  /* SIDE PANEL */
  .panel-side {
    position: relative;
    width: 240px; height: 700px;
    background: linear-gradient(180deg, #1566ae 0%, var(--blue-mid) 40%, var(--blue-deep) 100%);
    color: var(--white);
    font-family: "PT Sans Narrow", sans-serif;
    padding: 44px 22px 0;
  }
  .info-block { margin-bottom: 22px; }
  .info-block h3 {
    font-family: "Open Sans", sans-serif;
    font-size: 12px;
    font-weight: 700;
    margin-bottom: 3px;
  }
  .info-block p { font-size: 12px; line-height: 1.35; font-style: italic; }
  .follow {
    position: absolute;
    left: 22px; bottom: 104px;
    font-size: 12px;
  }
  .follow .invite { font-style: italic; margin-bottom: 4px; }
  .follow .handle {
    font-family: "Open Sans", sans-serif;
    font-weight: 700;
    font-size: 13px;
    display: flex; align-items: center; gap: 6px;
  }
  .follow .handle::before {
    content: "";
    width: 8px; height: 8px;
    background: var(--white);
    border-radius: 50%;
  }
  .barcode-area {
    position: absolute;
    left: 22px; bottom: 18px;
    width: 120px; height: 72px;
    background: var(--white);
  }

  /* TOP FLAP */
  .panel-top {
    width: 240px; height: 240px;
    background: var(--white);
    display: flex; align-items: center; justify-content: center;
    align-self: flex-start;
    margin-top: 25px;
  }
  .panel-top .brand-mark {
    color: var(--blue-text);
    font-weight: 800;
    font-size: 32px;
  }
</style>
</head>
<body>
<main class="dieline">

  <section class="panel-front" aria-label="Front panel">
    <div class="tag-freshness">
      <svg width="24" height="22" viewBox="0 0 24 22" aria-hidden="true">
        <path d="M4 20 C4 10 10 4 22 2 C20 14 14 20 4 20 Z" fill="none" stroke="#fff" stroke-width="2.2" stroke-linejoin="round"/>
        <path d="M4 20 L14 10" stroke="#fff" stroke-width="2" stroke-linecap="round"/>
      </svg>
      <span class="label">LASTING FRESHNESS</span>
    </div>

    <div class="brand-name">Spriza<span class="dot"></span></div>

    <div class="product-title">
      <div class="line-small">ALIGNER</div>
      <div class="line-large">CLEANER</div>
      <div class="supply-band">30-DAY SUPPLY</div>
    </div>

    <div class="aligner-art" role="img" aria-label="Clear dental aligner tray"></div>

    <div class="lower-white"></div>
    <div class="dot-field" role="img" aria-label="Soft halftone dot texture fading into white"></div>
    <svg class="wave-band" viewBox="0 0 240 70" preserveAspectRatio="none" aria-hidden="true">
      <path d="M0 0 C60 10 150 50 240 45 L240 70 C150 70 60 40 0 30 Z" fill="#ffffff"/>
      <path d="M0 0 C60 10 150 50 240 45 L240 58 C150 62 60 30 0 16 Z" fill="#1f3f9a"/>
      <path d="M0 0 C60 10 150 50 240 45 L240 50 C150 54 60 18 0 6 Z" fill="#2f6fd0"/>
    </svg>

    <ul class="benefits">
      <li><svg width="11" height="9" viewBox="0 0 11 9" aria-hidden="true"><path d="M1 4.5 L4 7.5 L10 1" fill="none" stroke="#1f57b5" stroke-width="2.2"/></svg>Easy-to-use</li>
      <li><svg width="11" height="9" viewBox="0 0 11 9" aria-hidden="true"><path d="M1 4.5 L4 7.5 L10 1" fill="none" stroke="#1f57b5" stroke-width="2.2"/></svg>5-minute Cleaning</li>
      <li><svg width="11" height="9" viewBox="0 0 11 9" aria-hidden="true"><path d="M1 4.5 L4 7.5 L10 1" fill="none" stroke="#1f57b5" stroke-width="2.2"/></svg>Lasting Freshness</li>
      <li><svg width="11" height="9" viewBox="0 0 11 9" aria-hidden="true"><path d="M1 4.5 L4 7.5 L10 1" fill="none" stroke="#1f57b5" stroke-width="2.2"/></svg>Portable Design</li>
    </ul>

    <div class="net-content">50ml &nbsp; ℮1.69 Fl Oz</div>
  </section>

  <section class="panel-side" aria-label="Side panel">
    <div class="info-block">
      <h3>Directions:</h3>
      <p>Remove aligners from mouth when eating or drinking. Dispense one pump of foam into each aligner. Place in the case for five minutes. Then, rinse aligners with water and wear again.</p>
    </div>
    <div class="info-block">
      <h3>Ingredients:</h3>
      <p>Water, Sodium Bicarbonate, Glycerin, PEG, Sodium Coco Sulfate, Sucralose, Sodium Citrate, Sodium Benzoate, EDTA Disodium Salt, Mentha Arvensis (Mint) Oil.</p>
    </div>
    <div class="info-block">
      <h3>Storage:</h3>
      <p>Store between 5°C and 35°C</p>
    </div>
    <div class="info-block">
      <h3>Manufactured By:</h3>
      <p>Corvale Tech Co., Ltd.<br>No. 42-3, Linden St.,<br>Eastvale Dist., Harbor City</p>
    </div>
    <div class="info-block">
      <h3>Imported By:</h3>
      <p>Spriza Trading Co., Ltd.<br>5th Floor, Tower 3, Maple Plaza,<br>No.210, Riverside Rd.,<br>Northgate Dist.</p>
    </div>
    <div class="follow">
      <p class="invite">Follow Us!</p>
      <p class="handle">Spriza</p>
      <p>www.spriza-care.example</p>
    </div>
    <div class="barcode-area" role="img" aria-label="Product barcode area"></div>
  </section>

  <section class="panel-top" aria-label="Top flap">
    <span class="brand-mark">Spriza</span>
  </section>

</main>
</body>
</html>
```